Banner Ad and Digital Ad design for tradeshow

I need two graphics designed (can be same/similar design just different dimensions. We are an engineering firm practicing in the solid waste industry. We are a conference sponsor and need two graphics.
(1) Banner Ad - 300x250 - gif, png, jped, html, or other. Imagery with our mantra - Driven by purpose. Guided by stewardship. Striving for excellence.
(2) Digital Ad (static) - 1920x1080 hi-res jpg or png.

Target Market(s)

Solid Waste Management Industry (Environmental)

Industry/Entity Type

Environmental

Requirements
Must have
• Quality Aesthetic
Nice to have
• Great Imagery + our mantra

```html
<!DOCTYPE html>
<html lang="en">
<head>
<meta charset="UTF-8">
<title>Guided by Stewardship – Tradeshow Ad</title>
<link href="https://fonts.googleapis.com/css2?family=Poppins:wght@400;800&display=swap" rel="stylesheet">
<style>
  :root {
    --page-bg: #e6e6e6;
    --sky-top: #6f5c9e;
    --sky-violet: #a56fae;
    --sky-pink: #e77fa4;
    --sky-coral: #f1866f;
    --sky-amber: #f6a55a;
    --ground: #0a0a0a;
    --title-fill: #e7a9cc;
    --title-shadow: rgba(40, 20, 50, 0.75);
    --emblem-fill: #070707;
    --badge-text: #ffffff;
  }
  * { margin: 0; padding: 0; box-sizing: border-box; }
  html, body {
    width: 1200px;
    height: 1200px;
    overflow: hidden;
    background: var(--page-bg);
  }
  .ad {
    position: absolute;
    left: 50px;
    top: 141px;
    width: 1100px;
    height: 918px;
    overflow: hidden;
  }
  .ad__scene {
    position: absolute;
    inset: 0;
    background: linear-gradient(180deg,
      var(--sky-top) 0%,
      var(--sky-violet) 14%,
      var(--sky-pink) 38%,
      var(--sky-coral) 58%,
      var(--sky-amber) 68%,
      var(--sky-coral) 70.5%,
      var(--ground) 71%,
      var(--ground) 100%);
  }
  .ad__bands {
    position: absolute;
    inset: 0;
    width: 100%;
    height: 100%;
  }
  .ad__mantra {
    position: absolute;
    left: 0;
    right: 0;
    top: 68px;
    text-align: center;
    font-family: "Poppins", sans-serif;
    font-weight: 800;
    color: var(--title-fill);
    text-transform: uppercase;
    text-shadow: 3px 4px 6px var(--title-shadow);
    line-height: 1;
  }
  .ad__mantra-main {
    display: block;
    font-size: 110px;
    line-height: 104px;
    letter-spacing: 1px;
  }
  .ad__mantra-sub {
    display: block;
    margin-top: 14px;
    font-size: 58px;
    letter-spacing: 1px;
  }
  .ad__badge {
    position: absolute;
    left: 329px;
    top: 381px;
    width: 442px;
    height: 159px;
  }
  .ad__emblem {
    position: absolute;
    inset: 0;
    background: var(--emblem-fill);
    border-radius: 40% 40% 14px 14px / 60% 60% 14px 14px;
  }
  .ad__tagline {
    position: absolute;
    left: 0;
    right: 0;
    top: 82px;
    text-align: center;
    font-family: "Poppins", sans-serif;
    font-weight: 400;
    font-size: 23px;
    line-height: 30px;
    color: var(--badge-text);
  }
</style>
</head>
<body>
  <main class="ad">
    <div class="ad__scene" role="img" aria-label="Photograph of a pink and violet sunset sky over a landfill site, with silhouettes of an excavator and haul trucks on the horizon"></div>

    <svg class="ad__bands" viewBox="0 0 1100 918" preserveAspectRatio="none" aria-hidden="true">
      <polygon points="0,0 200,0 0,120" fill="#5b4d9a" opacity="0.35"/>
      <polygon points="250,0 470,0 0,270 0,150" fill="#7f6bc0" opacity="0.35"/>
      <polygon points="1100,380 1100,560 600,918 330,918" fill="#ffffff" opacity="0.12"/>
      <polygon points="1100,600 1100,918 600,918" fill="#ffffff" opacity="0.06"/>
    </svg>

    <h1 class="ad__mantra">
      <span class="ad__mantra-main">Guided by<br>Stewardship.</span>
      <span class="ad__mantra-sub">Striving for excellence.</span>
    </h1>

    <div class="ad__badge">
      <div class="ad__emblem" role="img" aria-label="Black emblem of a landfill mound with vertical lines"></div>
      <p class="ad__tagline">- Driven by purpose.</p>
    </div>
  </main>
</body>
</html>
```